Design business card two side.
Simple and modern design like:

https://media.layoutvane.com/wp-content/uploads/2016/09/12062906/Modern-Design-Business-Card-Template.jpg
https://c7.plorvix.net/jpg/01/84/37/46/500_F_184374698_YLFWErxqrO1rgFAP7l9cvpWwpbOhgdU5.jpg
https://www.draftbinlist.com/wp-content/uploads/2017/04/Modern-Business-Card-Design-Template-5.jpg
http://kwm.pixelharborlane.com/wp-content/uploads/2013/03/modern+business+cards+13.jpg

Logo can be found in two types.

```html
<!DOCTYPE html>
<html lang="en">
<head>
<meta charset="utf-8">
<title>Kettle Labs — Business Card</title>
<link rel="stylesheet" href="https://fonts.googleapis.com/css2?family=Oswald:wght@500&family=Lato:wght@400;700&display=swap">
<style>
  :root {
    --canvas: #3b3b3d;
    --ink: #0b0b0c;
    --paper: #fbfcfd;
    --brand: #3aaee0;
    --brand-faint: #dbe9f4;
    --text-dark: #1d1d1f;
    --ghost-dark: #1f1f21;
    --muted-light: #c9c9cc;
  }
  * { box-sizing: border-box; margin: 0; padding: 0; }
  html, body { width: 1200px; height: 939px; overflow: hidden; }
  body { background: var(--canvas); position: relative; font-family: "Lato", sans-serif; }

  .card { position: absolute; top: 160px; width: 370px; height: 620px; border-radius: 6px; overflow: hidden; background: var(--ink); }
  .card--front { left: 195px; }
  .card--back { left: 635px; }
  .card-art { position: absolute; inset: 0; width: 100%; height: 100%; }

  .brand-name { position: absolute; left: 0; right: 0; text-align: center; font-family: "Oswald", sans-serif; font-weight: 500; color: var(--brand); letter-spacing: 3px; }
  .card--front .brand-name { top: 150px; font-size: 34px; right: 40px; }
  .card--back .brand-name { top: 110px; font-size: 34px; }

  .front-content { position: absolute; left: 0; right: 40px; text-align: center; color: var(--text-dark); }
  .person { top: 262px; }
  .person-name { font-family: "Oswald", sans-serif; font-weight: 500; font-size: 22px; letter-spacing: 1px; color: var(--brand); }
  .person-title { font-size: 13px; margin-top: -2px; }

  .contact-icons { top: 330px; display: flex; justify-content: center; gap: 10px; }
  .icon { width: 22px; height: 22px; }

  .contact-lines { top: 372px; font-size: 13.5px; line-height: 18px; letter-spacing: .3px; }
  .pin { top: 440px; display: flex; justify-content: center; }
  .address { top: 478px; font-size: 13.5px; line-height: 18px; }

  .back-url {
    position: absolute; right: 22px; bottom: 40px;
    writing-mode: vertical-rl; transform: rotate(180deg);
    font-size: 11px; line-height: 14px; letter-spacing: 4px;
    color: var(--muted-light); white-space: nowrap;
  }
</style>
</head>
<body>

<section class="card card--front" aria-label="Card front">
  <svg class="card-art" viewBox="0 0 370 620" aria-hidden="true">
    <defs>
      <clipPath id="paper-shape">
        <path d="M0 70 C0 25 30 0 80 0 L250 0 C325 50 360 170 360 310 C360 450 325 570 250 620 L0 620 Z"/>
      </clipPath>
    </defs>
    <path d="M0 70 C0 25 30 0 80 0 L250 0 C325 50 360 170 360 310 C360 450 325 570 250 620 L0 620 Z" fill="var(--paper)"/>
    <g clip-path="url(#paper-shape)">
      <text x="120" y="470" font-family="Oswald, sans-serif" font-weight="500" font-size="300" fill="var(--brand-faint)" transform="rotate(-90 120 470)">LABS</text>
    </g>
    <text x="366" y="585" font-family="Oswald, sans-serif" font-weight="500" font-size="60" fill="var(--ghost-dark)" transform="rotate(-90 366 585)">LA</text>
  </svg>

  <div class="brand-name">KETTLE LABS</div>

  <div class="front-content person">
    <div class="person-name">MARA QUILL</div>
    <div class="person-title">President</div>
  </div>

  <div class="front-content contact-icons">
    <svg class="icon" viewBox="0 0 22 22" aria-label="Phone"><circle cx="11" cy="11" r="10" fill="none" stroke="var(--text-dark)" stroke-width="1.4"/><path d="M7.5 6.5 L9.5 6.5 L10.3 9 L9 10 C9.6 11.4 10.6 12.4 12 13 L13 11.7 L15.5 12.5 L15.5 14.5 C10.5 15 7 11.5 7.5 6.5 Z" fill="var(--text-dark)"/></svg>
    <svg class="icon" viewBox="0 0 22 22" aria-label="Email"><circle cx="11" cy="11" r="10" fill="none" stroke="var(--text-dark)" stroke-width="1.4"/><rect x="6" y="7.5" width="10" height="7" fill="var(--text-dark)"/><path d="M6 7.5 L11 11.5 L16 7.5" fill="none" stroke="var(--paper)" stroke-width="1"/></svg>
    <svg class="icon" viewBox="0 0 22 22" aria-label="Website"><circle cx="11" cy="11" r="10" fill="none" stroke="var(--text-dark)" stroke-width="1.4"/><circle cx="11" cy="11" r="5.5" fill="var(--text-dark)"/><path d="M5.5 11 H16.5 M11 5.5 C8.5 8 8.5 14 11 16.5 M11 5.5 C13.5 8 13.5 14 11 16.5" fill="none" stroke="var(--paper)" stroke-width=".8"/></svg>
  </div>

  <div class="front-content contact-lines">
    <div>0123 456 789</div>
    <div>info@kettlelabs.ca</div>
    <div>www.kettlelabs.ca</div>
  </div>

  <div class="front-content pin">
    <svg class="icon" viewBox="0 0 22 22" aria-label="Address"><circle cx="11" cy="11" r="10.5" fill="var(--text-dark)"/><path d="M11 5 C8.5 5 7 6.8 7 8.8 C7 11.5 11 16.5 11 16.5 C11 16.5 15 11.5 15 8.8 C15 6.8 13.5 5 11 5 Z" fill="var(--paper)"/><circle cx="11" cy="8.8" r="1.6" fill="var(--text-dark)"/></svg>
  </div>

  <div class="front-content address">
    <div>123, Street Address,</div>
    <div>Zip Code, Canada.</div>
  </div>
</section>

<section class="card card--back" aria-label="Card back">
  <svg class="card-art" viewBox="0 0 370 620" aria-hidden="true">
    <text x="150" y="600" font-family="Oswald, sans-serif" font-weight="500" font-size="190" fill="var(--ghost-dark)" transform="rotate(-90 150 600)">KETTLE</text>
    <text x="300" y="430" font-family="Oswald, sans-serif" font-weight="500" font-size="56" fill="var(--ghost-dark)" letter-spacing="8" transform="rotate(-90 300 430)">LABS</text>
  </svg>
  <div class="brand-name">KETTLE LABS</div>
  <div class="back-url">www.kettlelabs.ca</div>
</section>

</body>
</html>
```